Fontenot Bayou Grillhouse (Owners Card)

Need a classy, but modern business card. I have included a promotional card for the steakhouse. I need one for myself (the owner) that is more professional.

Target Market(s)

General Public

Industry/Entity Type

Food service

Contact Information for Business Card

Name, business address, phone number, email, logo

Font styles to use
Serif
Sans Serif
Decorative
Script

Requirements
Must have
• My name (Darvel Pruitt), business address (327 Oakmere Street), phone number (510) 493-2615, email (Dpruittkr4@mailvane.example. On the back of the card: Psalms 27 1 The LORD is my light and my salvation— whom shall I fear? The LORD is the stronghold of my life— of whom shall I be afraid? 2 When the wicked advance against me to devour me, it is my enemies and my foes who will stumble and fall. 3 Though an army besiege me, my heart will not fear; though war break out against me, even then I will be confident.
Nice to have
• Something that’s bold, but modern and professional.

```html
<!DOCTYPE html>
<html lang="en">
<head>
<meta charset="utf-8">
<title>Fontenot Bayou Grillhouse – Owner Card</title>
<link rel="stylesheet" href="https://fonts.googleapis.com/css2?family=Cinzel:wght@400;700&family=Open+Sans:wght@400;700&display=swap">
<style>
  :root {
    --stage: #3a3a3a;
    --card: #050505;
    --green: #8dc63f;
    --gold: #e2b32a;
    --orange: #f7941d;
    --red: #ef4136;
    --pink: #d4145a;
    --ink: #111111;
    --white: #ffffff;
  }
  * { box-sizing: border-box; margin: 0; padding: 0; }
  html, body { width: 1200px; height: 901px; overflow: hidden; }
  body {
    background: var(--stage);
    font-family: "Open Sans", Arial, sans-serif;
    position: relative;
  }
  .card {
    position: absolute;
    left: 280px;
    width: 640px;
    height: 366px;
    background: var(--card);
    border-radius: 26px;
    overflow: hidden;
  }
  .card--back { top: 40px; }
  .card--front { top: 456px; }

  .brand {
    display: flex;
    align-items: center;
    gap: 12px;
    font-family: "Cinzel", Georgia, serif;
    font-weight: 700;
    color: var(--orange);
    letter-spacing: 1px;
    white-space: nowrap;
  }
  .brand__dot {
    border-radius: 50%;
    background: var(--orange);
    flex: none;
  }
  .card--back .brand {
    position: absolute;
    top: 28px; left: 0; right: 0;
    justify-content: center;
    font-size: 24px;
  }
  .card--back .brand__dot { width: 14px; height: 14px; }

  .verse-title {
    position: absolute;
    top: 76px; left: 0; right: 0;
    text-align: center;
    color: var(--white);
    font-weight: 700;
    font-size: 15px;
  }
  .verse-panel {
    position: absolute;
    left: 30px; right: 22px; bottom: 18px;
    height: 234px;
    border-radius: 24px;
    background: linear-gradient(90deg, var(--green) 0%, var(--gold) 35%, var(--orange) 60%, var(--red) 82%, var(--pink) 100%);
    padding: 26px 26px 18px 20px;
    color: var(--ink);
    font-size: 14.5px;
    line-height: 1.55;
  }
  .verse {
    display: grid;
    grid-template-columns: 26px 1fr;
    margin-bottom: 10px;
  }
  .verse__num { font-size: 13px; padding-top: 1px; }

  .card--front .brand {
    position: absolute;
    top: 48px; left: 44px;
    font-size: 30px;
  }
  .emblem {
    position: absolute;
    top: 122px; right: 40px;
    width: 190px; height: 190px;
    border-radius: 50%;
    background: var(--orange);
  }

  .owner-name {
    position: absolute;
    top: 150px; left: 44px;
    font-family: "Cinzel", Georgia, serif;
    font-weight: 700;
    font-size: 30px;
    letter-spacing: 1px;
    background: linear-gradient(90deg, #fff200, var(--orange) 45%, var(--red));
    -webkit-background-clip: text;
    background-clip: text;
    color: transparent;
  }
  .contact-list {
    position: absolute;
    top: 214px; left: 44px;
    list-style: none;
    color: var(--white);
    font-size: 18px;
    line-height: 1;
  }
  .contact-list li {
    display: flex;
    align-items: center;
    gap: 14px;
    margin-bottom: 14px;
  }
  .contact-list svg { width: 18px; height: 18px; flex: none; }
</style>
</head>
<body>

<section class="card card--back">
  <div class="brand"><span class="brand__dot"></span>Fontenot Bayou Grillhouse</div>
  <h2 class="verse-title">Psalms 27</h2>
  <div class="verse-panel">
    <p class="verse"><span class="verse__num">1</span><span>The LORD is my light and my salvation— whom shall I fear? The LORD is the stronghold of my life— of whom shall I be afraid?</span></p>
    <p class="verse"><span class="verse__num">2</span><span>When the wicked advance against me to devour me, it is my enemies and my foes who will stumble and fall.</span></p>
    <p class="verse"><span class="verse__num">3</span><span>Though an army besiege me, my heart will not fear; though war break out against me, even then I will be confident.</span></p>
  </div>
</section>

<section class="card card--front">
  <div class="brand">Fontenot Bayou Grillhouse</div>
  <span class="emblem" aria-hidden="true"></span>
  <h1 class="owner-name">DARVEL PRUITT</h1>
  <ul class="contact-list">
    <li>
      <svg viewBox="0 0 24 24" aria-hidden="true"><path fill="#f7941d" d="M6.6 10.8a15.1 15.1 0 0 0 6.6 6.6l2.2-2.2c.3-.3.7-.4 1-.2 1.1.4 2.3.6 3.6.6.6 0 1 .4 1 1V20c0 .6-.4 1-1 1A17 17 0 0 1 3 4c0-.6.4-1 1-1h3.5c.6 0 1 .4 1 1 0 1.3.2 2.5.6 3.6.1.3 0 .7-.2 1z"/></svg>
      (510) 493-2615
    </li>
    <li>
      <svg viewBox="0 0 24 24" aria-hidden="true"><rect x="2" y="5" width="20" height="14" rx="1.5" fill="#ef4136"/><path d="M2.5 6l9.5 7 9.5-7" fill="none" stroke="#050505" stroke-width="1.6"/></svg>
      Dpruittkr4@mailvane.example
    </li>
    <li>
      <svg viewBox="0 0 24 24" aria-hidden="true"><path fill="#ef4136" d="M12 2a7 7 0 0 0-7 7c0 5.2 7 13 7 13s7-7.8 7-13a7 7 0 0 0-7-7zm0 9.5A2.5 2.5 0 1 1 12 6.5a2.5 2.5 0 0 1 0 5z"/></svg>
      327 Oakmere Street
    </li>
  </ul>
</section>

</body>
</html>
```